Sophisticated, clean website reflecting my feminine, playful side to sell my abstract art,

I need a website no more than 3 pages to showcase my paintings, a little about me and some contact info. I do abstracts so looking for something a little edgy, yet feminine and current.
Updates

Hi there, These are some artists websites that I Iike: Marlowevint.com (I like how airy it is) rupertalcombe.com gideonparvell.com (I like how it scrolls) I'll need a place for a photo ( a headshot-i do not have it yet so I'll need to be able to upload that later) as well as an area for my bio. Also, it's important that I will be able to upload any new photos and descriptions easily so it should be user friendly. Lastly, I like in a sunny place so would like to have this seem upbeat and playful as that is how i like to paint. thanks-I'm trying to upload my photos now -

Target Market(s)

ppl ages 35-70 who want large scale art for their homes

Industry/Entity Type

art

Coding

Coded - Design and coding required

Number of Pages Required

3 page

Colors

Designer to choose colors to be used in the design.

Requirements
Must have
• photos of my art, a place for my bio, be easy to reach me. tasteful-nothing too "in your face" -my clients are pretty high end and organized. They like clean lines
Nice to have
• sophisticated background, muted tones in the back-similar clean font throughout-no cursive
Should not have
• too many dark areas. Too many blocks of color. Too serious.

```html
<!DOCTYPE html>
<html lang="en">
<head>
<meta charset="utf-8">
<title>Hazel Sorrento — Abstract Art</title>
<link rel="stylesheet" href="https://fonts.googleapis.com/css2?family=Oswald:wght@200;300&family=Questrial&display=swap">
<style>
  :root {
    --ink: #3a3a3a;
    --ink-soft: #555555;
    --rule: #cfcfcf;
    --header-bg: #ffffff;
    --page-top: #f7f7f7;
    --page-bottom: #efeeed;
    --arrow-light: #ffffff;
    --arrow-grey: #8a8a8a;
    --hero-green: #5a9a4a;
    --hero-teal: #1f7f7a;
    --hero-pale: #e6ebe4;
    --gallery-blue: #4a8fc4;
    --gallery-ochre: #d2a33c;
    --gallery-pale: #eef0ee;
    --portrait-grey: #d8d8d8;
  }
  * { box-sizing: border-box; margin: 0; padding: 0; }
  html, body { width: 1200px; height: 3085px; overflow: hidden; }
  body {
    position: relative;
    font-family: "Questrial", sans-serif;
    color: var(--ink);
    background: linear-gradient(180deg, var(--page-top) 843px, var(--page-bottom) 3085px);
  }
  .site-header {
    position: absolute; top: 0; left: 0; width: 1200px; height: 116px;
    background: var(--header-bg);
    border-bottom: 1px solid var(--rule);
    display: flex; align-items: center; justify-content: center; gap: 20px;
  }
  .brand-name {
    font-family: "Questrial", sans-serif;
    font-size: 50px; letter-spacing: 3px; color: var(--ink-soft);
  }
  .brand-mark { width: 34px; height: 44px; background: var(--ink); }
  .main-nav {
    position: absolute; top: 117px; left: 0; width: 1200px; height: 65px;
    background: var(--header-bg);
  }
  .main-nav a {
    position: absolute; top: 14px; transform: translateX(-50%);
    font-family: "Oswald", sans-serif; font-weight: 300;
    font-size: 24px; color: var(--ink-soft); text-decoration: none;
    padding-bottom: 3px;
  }
  .main-nav a.active { border-bottom: 2px solid var(--ink); color: var(--ink); }
  .hero {
    position: absolute; top: 182px; left: 0; width: 1200px; height: 661px;
    background:
      radial-gradient(ellipse at 30% 30%, var(--hero-green), transparent 60%),
      radial-gradient(ellipse at 80% 60%, var(--hero-teal), transparent 55%),
      var(--hero-pale);
  }
  .arrow { position: absolute; width: 30px; height: 50px; }
  .arrow path { fill: none; stroke-width: 3; stroke-linecap: round; stroke-linejoin: round; }
  .hero .arrow path { stroke: var(--arrow-light); }
  .section-title {
    position: absolute; left: 0; width: 1200px; text-align: center;
    font-family: "Oswald", sans-serif; font-weight: 300;
    font-size: 66px; letter-spacing: 1px; color: var(--ink); line-height: 1;
  }
  .title-rule { position: absolute; height: 2px; background: var(--ink-soft); opacity: .7; }
  .portrait {
    position: absolute; left: 104px; top: 1083px; width: 326px; height: 377px;
    background: linear-gradient(180deg, #e6e6e6, var(--portrait-grey));
  }
  .bio {
    position: absolute; left: 477px; top: 1084px; width: 620px;
    font-size: 18.5px; line-height: 28.3px; color: var(--ink-soft); text-align: justify;
  }
  .bio p + p { margin-top: 15px; }
  .artwork {
    position: absolute; left: 146px; top: 1733px; width: 908px; height: 561px;
    background:
      radial-gradient(circle at 20% 60%, var(--gallery-ochre), transparent 32%),
      radial-gradient(circle at 85% 75%, var(--gallery-ochre), transparent 28%),
      radial-gradient(ellipse at 55% 30%, var(--gallery-blue), transparent 45%),
      var(--gallery-pale);
  }
  .gallery .arrow path { stroke: var(--arrow-grey); stroke-width: 2.5; }
  .contact-item {
    position: absolute; top: 2655px; width: 280px; transform: translateX(-50%);
    text-align: center; font-size: 19.5px; color: var(--ink);
  }
  .contact-item svg { display: block; margin: 0 auto 18px; width: 44px; height: 44px; }
  .contact-item svg * { fill: none; stroke: var(--ink); stroke-width: 1.6; }
  .site-footer {
    position: absolute; top: 3004px; left: 0; width: 1200px; height: 81px;
    border-top: 1px solid var(--rule);
    text-align: center; padding-top: 30px; font-size: 15.5px; color: var(--ink);
  }
</style>
</head>
<body>
  <header class="site-header">
    <span class="brand-name">HAZEL</span>
    <span class="brand-mark"></span>
    <span class="brand-name">SORRENTO</span>
  </header>

  <nav class="main-nav">
    <a class="active" href="#" style="left:272px">HOME</a>
    <a href="#" style="left:471px">ABOUT ME</a>
    <a href="#" style="left:681px">GALLERY</a>
    <a href="#" style="left:902px">CONTACT ME</a>
  </nav>

  <section class="hero" role="img" aria-label="Featured abstract painting in greens, teals and rust brushstrokes">
    <svg class="arrow" style="left:22px;top:478px" viewBox="0 0 30 50"><path d="M24 4 L6 25 L24 46"/></svg>
    <svg class="arrow" style="left:1140px;top:478px" viewBox="0 0 30 50"><path d="M6 4 L24 25 L6 46"/></svg>
  </section>

  <section class="about">
    <h2 class="section-title" style="top:948px">ABOUT THE ARTIST</h2>
    <div class="title-rule" style="left:399px;top:1021px;width:391px"></div>
    <div class="portrait" role="img" aria-label="Black and white portrait photo of the artist"></div>
    <div class="bio">
      <p>Lorem ipsum dolor sit amet, consectetur adipiscing elit, sed do eiusmod tempor incididunt ut labore et dolore magna aliqua. Ut enim ad minim veniam, quis nostrud exercitation Lorem ipsum dolor sit amet, consectetur adipiscing elit, sed do eiusmod tempor incididunt ut labore et dolore</p>
      <p>Duis aute irure dolor in reprehenderit in voluptate velit esse cillum dolore eu fugiat nulla pariatur. Excepteur sint occaecat cupidatat non proident, sunt in culpa qui officia deserunt mollit anim id est laborum.</p>
      <p>Sed ut perspiciatis unde pariatur. Excepteur sint occaecat cupidatat non proident, sunt in culpa qui officia deserunt mollit anim id est laborum.enderit in voluptate velit esse cillum dolore eu fugiat nulla pariatur. Excepteur sint occaecat cupidatat non proident, sunt in culpa qui officia fficia deserunt mollit anim id est laborum. Sed ut perspiciatis unde pariatur.</p>
    </div>
  </section>

  <section class="gallery">
    <h2 class="section-title" style="top:1608px;left:-14px">GALLERY</h2>
    <div class="title-rule" style="left:500px;top:1684px;width:171px"></div>
    <div class="artwork" role="img" aria-label="Abstract painting with ochre, rust and blue swirls on a pale ground"></div>
    <svg class="arrow" style="left:64px;top:1988px" viewBox="0 0 30 50"><path d="M24 4 L6 25 L24 46"/></svg>
    <svg class="arrow" style="left:1108px;top:1988px" viewBox="0 0 30 50"><path d="M6 4 L24 25 L6 46"/></svg>
  </section>

  <section class="contact">
    <h2 class="section-title" style="top:2473px">CONTACT ME</h2>
    <div class="title-rule" style="left:472px;top:2553px;width:259px"></div>

    <div class="contact-item" style="left:260px">
      <svg viewBox="0 0 44 44"><rect x="3" y="9" width="38" height="26"/><path d="M3 9 L22 25 L41 9 M3 35 L17 21 M41 35 L27 21"/></svg>
      info@hazelsorrento.com
    </div>
    <div class="contact-item" style="left:550px">
      <svg viewBox="0 0 44 44"><path d="M10 4 L16 12 L12 17 C15 24 20 29 27 32 L32 28 L40 34 L35 41 C20 39 6 25 4 10 Z"/><path d="M24 10 A10 10 0 0 1 34 20 M24 4 A16 16 0 0 1 40 20"/></svg>
      Phone: (555) 014 2286
    </div>
    <div class="contact-item" style="left:781px">
      <svg viewBox="0 0 44 44"><circle cx="22" cy="22" r="17"/></svg>
      @hsorrentoart
    </div>
    <div class="contact-item" style="left:1002px">
      <svg viewBox="0 0 44 44"><circle cx="22" cy="22" r="17"/></svg>
      @hzpainter
    </div>
  </section>

  <footer class="site-footer">© 2022 Hazel Sorrento &nbsp; All Rights Reserved</footer>
</body>
</html>
```